Clikora - photography in NYC - leveraging big data and robotics

We've got a photography business in NYC. It is kind of on-demand photographers, but actually is just five of us who work as a team. Over the last three years we've taken tens of thousands of photographs and are now sitting on a load of great work. We want to leverage that in a way that lets people book either by event type or location. So, they would click on Harlow Green and a load of examples of our work would pop up. Or Wedding Shower, and relevant examples would pop up. We've got the pictures structured pretty well to enable this. Now we just need a website that illustrates this and then leads through the booking process (time, location, date, contact etc.) and payment.

Target Market(s)

Everyone - corporates, real estate, tourists, families, headshots, bloggers, products, wedding showers, baby showers, engagements, venues, restaurants/bars, holiday pictures, City Hall weddings, kids birthday parties, adult birthday parties, PR companies, corporate events.... long list.

Industry/Entity Type

Photographer

Number of Pages Required

5+ page

Colors

Designer to choose colors to be used in the design.

Requirements
Must have
• A great, engaging landing page which people can choose by event type or location. This would then pull in examples of our work in that location or in that event type. Then they go through the booking process. This is simple capturing key details - see here https://clikora.example/book/
Nice to have
• Social links
Should not have
• Nothing specific.

```html
<!DOCTYPE html>
<html lang="en">
<head>
<meta charset="utf-8">
<title>Clikora — Photography in NYC</title>
<link href="https://fonts.googleapis.com/css2?family=Montserrat:wght@500;600;700;800&family=Nunito+Sans:wght@400;600;700&display=swap" rel="stylesheet">
<style>
:root{
  --red:#b3141f;
  --red-dark:#8f0f18;
  --ink:#222;
  --muted:#555;
  --line:#e3e3e3;
  --paper:#ffffff;
  --soft:#f5f5f5;
  --shade:#ececec;
}
*{box-sizing:border-box;margin:0;padding:0}
html,body{width:1200px;height:3991px;overflow:hidden}
body{position:relative;background:var(--paper);font-family:"Nunito Sans",Arial,sans-serif;color:var(--ink)}
.abs{position:absolute}
h2,h3,.heading{font-family:"Montserrat",Arial,sans-serif}
.btn{position:absolute;display:flex;align-items:center;justify-content:center;background:var(--red);color:#fff;font-family:"Montserrat",Arial,sans-serif;font-weight:700;font-size:11px;border-radius:3px}
.btn-outline{background:#fff;color:var(--red);border:2px solid var(--red)}
.photo{position:absolute;border:6px solid #fff;box-shadow:0 6px 18px rgba(0,0,0,.22)}

/* nav */
.site-nav{position:absolute;top:0;left:0;width:1200px;height:64px;background:#fff;box-shadow:0 2px 8px rgba(0,0,0,.06)}
.nav-link{position:absolute;top:24px;font-size:12px;font-weight:600;color:#333}
.brand{position:absolute;top:19px;left:565px;width:100px;text-align:center;font-family:"Montserrat",Arial,sans-serif;font-weight:800;font-size:18px;color:var(--red);letter-spacing:.5px}

/* hero */
.hero-title{position:absolute;top:88px;left:0;width:1200px;text-align:center;font-size:20px;font-weight:700;color:#1b1b1b}
.play{position:absolute;left:581px;top:280px;width:44px;height:44px;border-radius:50%;background:var(--red);display:flex;align-items:center;justify-content:center}

/* section titles */
.sec-title{position:absolute;left:0;width:1200px;text-align:center;color:var(--red);font-weight:700;font-size:22px;line-height:1.3}
.lead{position:absolute;left:300px;width:600px;text-align:center;font-size:12px;line-height:1.75;color:#333}

.feature{position:absolute;top:733px;width:236px;height:148px;background:#fff;box-shadow:0 3px 14px rgba(0,0,0,.1);text-align:center;padding-top:20px}
.feature h3{color:var(--red);font-size:13px;font-weight:700;margin-top:10px}
.feature p{font-size:10px;color:#555;margin:6px 30px 0;line-height:1.5}

.gray-band{position:absolute;left:0;width:1200px}

.map-area{position:absolute;left:234px;top:1168px;width:564px;height:442px;background:linear-gradient(150deg,#e2e2e6,#cbccd1);border-radius:6px}

.divider{position:absolute;left:168px;width:830px;height:1px;background:var(--line)}
.body-text{position:absolute;font-size:12px;line-height:1.85;color:#333}

.quote-card{position:absolute;left:617px;top:2030px;width:367px;height:152px;background:#fff;box-shadow:0 3px 16px rgba(0,0,0,.12);padding:20px 24px;font-style:italic;font-size:13px;line-height:1.6;color:#444}
.avatar{position:absolute;border-radius:50%;border:4px solid #fff;box-shadow:0 3px 10px rgba(0,0,0,.2)}

.team-card{position:absolute;top:2818px;width:265px;height:184px;background:#fff;box-shadow:0 3px 14px rgba(0,0,0,.1);text-align:center;padding-top:64px}
.team-card h3{color:var(--red);font-size:13px;font-weight:700}
.team-card p{font-size:10px;color:#444;line-height:1.5;margin:6px 28px 0}
.socials{display:flex;justify-content:center;gap:8px;margin-top:10px}
.socials span{width:8px;height:8px;border-radius:50%;background:var(--red)}

.faq{position:absolute;background:#fff;box-shadow:0 2px 10px rgba(0,0,0,.09);font-size:12px;color:#333;padding:12px 18px}
.faq .sign{position:absolute;right:18px;top:9px;font-size:16px;color:#666}
.faq .answer{margin-top:18px;font-size:10.5px;color:#555;line-height:1.6}

.contact-item{position:absolute;top:3676px;width:240px;text-align:center;font-size:12px;color:#333}
.field{position:absolute;border:1px solid #cfcfcf;background:#fff;font-size:10px;color:#777;padding:12px}
</style>
</head>
<body>

<nav class="site-nav">
  <span class="nav-link" style="left:300px">Home</span>
  <span class="nav-link" style="left:361px">About us</span>
  <span class="nav-link" style="left:437px">Gallery</span>
  <span class="nav-link" style="left:506px">FAQ</span>
  <span class="brand">CLIKORA</span>
  <span class="nav-link" style="left:708px">Blog</span>
  <span class="nav-link" style="left:764px">Contact</span>
  <span class="btn" style="left:842px;top:17px;width:88px;height:28px">Book Now</span>
</nav>

<header>
  <h1 class="hero-title heading">Capture the Moment you Care About</h1>
  <span class="btn" style="left:562px;top:122px;width:76px;height:26px">Book Now</span>
  <div class="photo" role="img" aria-label="Blurred portrait photo" style="left:186px;top:261px;width:181px;height:133px;border:none;background:linear-gradient(135deg,#6a7e95,#c9b2a0)"></div>
  <div class="photo" role="img" aria-label="Family walking on a lawn" style="left:277px;top:165px;width:150px;height:133px;background:linear-gradient(#b6c7c0,#6f8a5a)"></div>
  <div class="photo" role="img" aria-label="Small photo of a couple" style="left:697px;top:165px;width:100px;height:105px;background:linear-gradient(#ddd,#a9a39c)"></div>
  <div class="photo" role="img" aria-label="Wedding detail photo" style="left:790px;top:220px;width:132px;height:105px;background:linear-gradient(#f1ede8,#cfc5bb)"></div>
  <div class="photo" role="img" aria-label="Blurred couple photo" style="left:920px;top:226px;width:123px;height:93px;border:none;background:linear-gradient(#9aa0a8,#4d535a)"></div>
  <div class="photo" role="img" aria-label="Pet photo" style="left:790px;top:318px;width:132px;height:82px;background:linear-gradient(#c7a27a,#7a5b3e)"></div>
  <div class="photo" role="img" aria-label="Family video still by the waterfront" style="left:426px;top:181px;width:362px;height:245px;background:linear-gradient(#d8dde2,#b9a89a)"></div>
  <div class="play"><svg width="16" height="16" viewBox="0 0 16 16"><path d="M5 3l8 5-8 5z" fill="#fff"/></svg></div>
</header>

<section>
  <h2 class="sec-title" style="top:570px">We only small pool of hand Selected<br>photographers</h2>
  <p class="lead" style="top:638px">We only hire a small pool of hand-selected photographers. They are all highly skilled, kind and friendly. You will get your pictures within 48 hours. They will look great. We can be with you within an hour or on any day that suits you. Prices start from $49. You should hurry and book a photographer now.</p>
  <div class="feature" style="left:222px">
    <svg width="30" height="28" viewBox="0 0 30 28"><path d="M3 12h5v13H3zM10 24V12l6-9c2 0 3 1 3 3l-1 5h7c2 0 3 2 2 4l-3 8c-1 1-2 2-3 2z" fill="none" stroke="#b3141f" stroke-width="2"/></svg>
    <h3>Fast, easy, afordable.</h3>
    <p>Book now for your session within a few hours. Prices from $49.</p>
  </div>
  <div class="feature" style="left:482px">
    <svg width="28" height="28" viewBox="0 0 28 28"><rect x="3" y="5" width="22" height="20" rx="2" fill="none" stroke="#b3141f" stroke-width="2"/><path d="M3 10h22M9 2v6M19 2v6M9 17l4 4 7-7" fill="none" stroke="#b3141f" stroke-width="2"/></svg>
    <h3>We are always available</h3>
    <p>Book for today, tomorrow, next week, next month.</p>
  </div>
  <div class="feature" style="left:742px">
    <svg width="28" height="28" viewBox="0 0 28 28"><circle cx="14" cy="12" r="9" fill="none" stroke="#b3141f" stroke-width="2"/><path d="M9 20l-3 7 5-2 3 3 0-6M19 20l3 7-5-2" fill="none" stroke="#b3141f" stroke-width="2"/><path d="M10 12l3 3 5-6" fill="none" stroke="#b3141f" stroke-width="2"/></svg>
    <h3>100% Guarantee</h3>
    <p>People love us so we think you'll love us too. If not, we give your money back.</p>
  </div>
</section>

<section>
  <div class="gray-band" style="top:955px;height:1680px;background:linear-gradient(#eeeeee 0,#f7f7f7 40%,#fff 100%)"></div>
  <h2 class="sec-title" style="top:1018px">See Photo Examples by<br>Event or Place</h2>
  <span class="btn" style="left:470px;top:1093px;width:108px;height:27px">Choose Place</span>
  <span class="btn btn-outline" style="left:588px;top:1093px;width:108px;height:27px">Choose Event</span>

  <div class="map-area" role="img" aria-label="Map of New York with pinned photo locations"></div>
  <div class="photo" role="img" aria-label="Harlow Green park lawn" style="left:737px;top:1245px;width:200px;height:108px;border-width:4px;background:linear-gradient(#a9c3dd 0,#cfdbe4 35%,#6f9b4d 60%,#4f7d34)"></div>

  <div class="divider" style="top:1661px"></div>
</section>

<section>
  <div class="photo" role="img" aria-label="Two children outdoors in autumn" style="left:258px;top:1720px;width:314px;height:225px;background:linear-gradient(160deg,#d7b56a,#7b6a4c 60%,#4d4a40)"></div>
  <div class="photo" role="img" aria-label="Child walking in a snowy park" style="left:218px;top:1847px;width:182px;height:130px;background:linear-gradient(#dfe4ea,#b6bcc3 60%,#eef0f2)"></div>
  <h2 class="abs" style="left:628px;top:1712px;color:var(--red);font-size:21px;font-weight:700;line-height:1.3">So, Why after all Clikora<br>Was Started?</h2>
  <p class="body-text" style="left:628px;top:1780px;width:370px">It started with five friends who loved taking pictures around the city. We kept getting asked to shoot birthdays, weddings and family days, so we turned it into a team. Three years and tens of thousands of photos later, we still love every booking. Book us and see why.</p>

  <div class="abs" role="img" aria-label="Vintage camera" style="left:0;top:2044px;width:226px;height:199px;background:radial-gradient(circle at 60% 55%,#3a3a3a 0,#5b5b5b 30%,#cfcfcf 55%,rgba(255,255,255,0) 70%)"></div>
  <h2 class="abs" style="left:250px;top:2052px;width:310px;text-align:right;color:var(--red);font-size:21px;font-weight:700;line-height:1.3">Our Build Reputation<br>Among Clients</h2>
  <p class="body-text" style="left:250px;top:2118px;width:310px;text-align:right">We get a lot of great reviews on trusted sites and many repeat clients. You can check their stories, read what they liked and decide for yourself.</p>
  <div class="quote-card">Lorem ipsum dolor sit amet, consectetuer adipiscing elit. Aenean commodo ligula eget dolor. Aenean massa. Cum sociis natoque penatibus et magnis dis parturient montes
    <div class="abs" style="right:24px;bottom:16px;display:flex;gap:10px;font-style:normal;font-size:16px"><span style="color:#ccc">&larr;</span><span style="color:var(--red)">&rarr;</span></div>
    <div class="abs" style="left:24px;bottom:18px;display:flex;gap:5px"><span style="width:6px;height:6px;border-radius:50%;background:#ddd"></span><span style="width:6px;height:6px;border-radius:50%;background:#ddd"></span><span style="width:6px;height:6px;border-radius:50%;background:var(--red)"></span><span style="width:6px;height:6px;border-radius:50%;background:#ddd"></span></div>
  </div>
  <div class="avatar" role="img" aria-label="Client portrait" style="left:622px;top:2212px;width:46px;height:46px;border-width:2px;background:linear-gradient(#c98c64,#6b4a35)"></div>
  <p class="abs heading" style="left:676px;top:2220px;font-size:10px;font-weight:700;line-height:1.3">NINA<br>CASTELL</p>
</section>

<section>
  <div class="abs" role="img" aria-label="Photographer holding a camera in a field" style="left:0;top:2309px;width:1200px;height:345px;background:radial-gradient(ellipse at 50% 55%,#7a5e54 0,#b9a494 22%,#e6e2d6 45%,#f4f3ec 70%,#fff 100%)"></div>
  <h2 class="abs" style="left:0;top:2400px;width:1200px;text-align:center;font-size:24px;font-weight:700;color:#1d1d1d;line-height:1.3">We will Capture the Moment You Never<br>Imagined can be Captured</h2>
  <span class="btn" style="left:530px;top:2492px;width:140px;height:30px">Book Now</span>
</section>

<section>
  <div class="gray-band" style="top:2760px;height:332px;background:linear-gradient(#fff,#f2f2f2)"></div>
  <h2 class="sec-title" style="top:2707px;font-size:20px">Our Team Members</h2>
  <div class="team-card" style="left:213px"><h3>Elias M. Brandt</h3><p>Lorem ipsum dolor sit amet, consectetuer adipiscing elit. Aenean commodo ligula eget dolor. Aenean massa. Cum sociis</p><div class="socials"><span></span><span></span><span></span></div></div>
  <div class="team-card" style="left:493px"><h3>Marius Delacroix</h3><p>Lorem ipsum dolor sit amet, consectetuer adipiscing elit. Aenean commodo ligula eget dolor. Aenean massa. Cum sociis</p><div class="socials"><span></span><span></span><span></span></div></div>
  <div class="team-card" style="left:773px"><h3>Owen Reyes</h3><p>Lorem ipsum dolor sit amet, consectetuer adipiscing elit. Aenean commodo ligula eget dolor. Aenean massa. Cum sociis</p><div class="socials"><span></span><span></span><span></span></div></div>
  <div class="avatar" role="img" aria-label="Team member portrait" style="left:295px;top:2762px;width:100px;height:100px;background:linear-gradient(#e6a64a,#5a3a26)"></div>
  <div class="avatar" role="img" aria-label="Team member portrait" style="left:575px;top:2762px;width:100px;height:100px;background:linear-gradient(#bdbdbd,#3d3d3d)"></div>
  <div class="avatar" role="img" aria-label="Team member portrait" style="left:855px;top:2762px;width:100px;height:100px;background:linear-gradient(#9fc4e2,#8a6a4d)"></div>
</section>

<section>
  <h2 class="sec-title" style="top:3153px;font-size:20px">Frequently Asked Questions</h2>
  <div class="faq" style="left:223px;top:3214px;width:349px;height:45px">Do we get all photographs?<span class="sign">+</span></div>
  <div class="faq" style="left:223px;top:3275px;width:349px;height:40px">How many pictures do I get?<span class="sign">+</span></div>
  <div class="faq" style="left:223px;top:3330px;width:349px;height:120px">Printing and touch up?<span class="sign">&minus;</span><p class="answer">We do offer printing and touch up service, if you are interested</p></div>
  <div class="faq" style="left:590px;top:3214px;width:373px;height:45px">When I get them?<span class="sign">+</span></div>
  <div class="faq" style="left:590px;top:3275px;width:373px;height:120px">How do I get the pictures?<span class="sign">&minus;</span><p class="answer">You will get a full gallery of the pictures. All of the pictures are yours to download, keep, share and print. There are no watermarks, of course!</p></div>
  <div class="faq" style="left:590px;top:3412px;width:373px;height:38px">Anything else? <b style="color:var(--red)">Just ask here.</b></div>
</section>

<section>
  <div class="gray-band" style="top:3530px;height:461px;background:linear-gradient(#f1f1f1,#fafafa)"></div>
  <h2 class="sec-title" style="top:3604px;font-size:22px">Get in Touch<br>With us</h2>
  <div class="abs" role="img" aria-label="Camera resting on a surface" style="left:985px;top:3676px;width:140px;height:110px;transform:rotate(-18deg);border-radius:14px;background:linear-gradient(#d9d9d9,#bcbcbc);opacity:.7"></div>
  <div class="contact-item" style="left:240px">
    <svg width="18" height="24" viewBox="0 0 22 30"><path d="M11 0C5 0 0 5 0 11c0 8 11 19 11 19s11-11 11-19C22 5 17 0 11 0z" fill="#b3141f"/><circle cx="11" cy="11" r="4" fill="#f4f4f4"/></svg>
    <p style="margin-top:14px">1200 Example Avenue</p>
  </div>
  <div class="contact-item" style="left:460px">
    <svg width="24" height="24" viewBox="0 0 24 24"><rect x="1" y="5" width="22" height="15" rx="1" fill="#b3141f"/><path d="M2 6l10 8 10-8" fill="none" stroke="#f4f4f4" stroke-width="1.6"/></svg>
    <p style="margin-top:14px">support@clikora.example</p>
  </div>
  <div class="contact-item" style="left:680px">
    <svg width="22" height="24" viewBox="0 0 24 24"><path d="M6 2l4 5-2 3c1 3 3 5 6 6l3-2 5 4-2 4C10 22 2 14 2 4z" fill="#b3141f"/></svg>
    <p style="margin-top:14px">(555) 013 - 0174</p>
  </div>
  <div class="field" style="left:202px;top:3772px;width:365px;height:40px">Name</div>
  <div class="field" style="left:202px;top:3830px;width:365px;height:40px">Email</div>
  <div class="field" style="left:202px;top:3888px;width:365px;height:40px">Subject</div>
  <div class="field" style="left:590px;top:3772px;width:362px;height:156px">Message</div>
  <div class="divider" style="top:3981px;left:168px;background:#d8d8d8"></div>
</section>

</body>
</html>
```